Talbrook Family Adoption Fundraiser

The sole purpose of this card is to tell people about the fundraiser and direct them to the website that will allow them to participate.  No other contact information is needed.
Since our approach is through personal networking, this card is our sole marketing piece and needs to be effective.  We will use an image of the card for the email & Facebook outreaches we will do.  We have a very limited budget (thus the fundraiser).
We will need a quantity of 2,000 cards.  We dont need to pay for high gloss or metalic finishes, but we were thinking we probably would want a folded business card to give us more real estate to work with.
About the fundraiser (will help you understand the content needed):  Our family is adopting a young girl from Colombia, South America.  We need to raise about $15,000 to bring her home.  This fundraiser is something called a "Duck Race".  People will go to our website and 'purchase' ducks for the race.  For each duck, there will be a rubber duck in the 'race' with their own unique number on it.  On the day of the race, all of the ducks are dumped into a river.  The first ones to cross the finish line down stream is the winner.  The more ducks people put in the race in their name, the more chances they have to win the cash prizes.  We will video the race, and show it on our website.  The idea was to make this an effective and low maintenance fundraiser - nobody has to attend an event - people dont even need to know us, they only need to want to have a chance at the cash prize.  With that being said, here are some ideas of content:
- title:  "The Grand Paddle Dash"
- "Win 1 of 3 cash prizes totalling $1,000
- www.Welcoming Our Little One.example
- The Talbrook family is adopting a young girl from Colombia, South America, and needs your help to bring her home.
-  We could include a picture of her.
-  We have an icon of a Duck holding a Colombian flag - this is an icon our son created and must be used as the focal point.  We want our existing kids (3 boys) to be part of this and our son Colin love computer animation and drawing - he created the icon.
-  People can sponsor a duck in the race or simply make their own, individual donation through the website.
-  We are using duck puns like crazy - we will even have a duck pun contest and the winners get free additional ducks in the race.
-  We want our network to be able to use these cards to get others to participate because of the cause - even if they do not know us.  That is why we thought the folded cards would be good because we would have space to put our testimony.  If cost-prohibitive, then we will settle for a 2-sided card.
We are open to suggestions, but time is absolutely of the essence.  We just got approved by Colombia, but we only have 2 weeks left to network with folks in our schools before they are done for the year.  We need a very quick turn-around.

Updates
Due to a browser issue, the icon was not uploaded in my brief.  They are in the process of manually adding it to my brief now and should be available shortly. Thank you for your help.

Target Market(s)
Potential donors/sponsors
Industry/Entity Type
Real Estate
Contact Information for Business Card
www.WelcomingOurLittleOne.example
Requirements
Must have
- Catchy but simple exterior to make people want to see the interior of a folded business card.

```html
<!DOCTYPE html>
<html lang="en">
<head>
<meta charset="utf-8">
<title>The Grand Paddle Dash – Fundraiser Card</title>
<link href="https://fonts.googleapis.com/css2?family=Open+Sans:wght@400;600;700;800&display=swap" rel="stylesheet">
<style>
  :root {
    --page-bg: #d9d9d9;
    --sun-core: #fffbe6;
    --sun-mid: #fde98a;
    --sun-edge: #f2c53a;
    --ink: #111111;
    --prize-red: #e8202a;
    --title-navy: #1c1f4a;
    --band-blue: #1e8fd0;
    --band-blue-dark: #0f5fa8;
    --white: #ffffff;
    --duck-yellow: #f6e43a;
    --flag-blue: #2a3f9c;
    --flag-red: #d42a2a;
  }
  * { box-sizing: border-box; margin: 0; padding: 0; }
  html, body { width: 1200px; height: 1097px; overflow: hidden; }
  body {
    background: var(--page-bg);
    font-family: "Open Sans", Arial, sans-serif;
    position: relative;
  }
  .card {
    position: absolute;
    left: 150px;
    width: 900px;
    height: 514px;
    overflow: hidden;
    background: radial-gradient(circle at 50% 45%, var(--sun-core) 0%, var(--sun-mid) 45%, var(--sun-edge) 100%);
    box-shadow: 0 4px 14px rgba(0,0,0,0.25);
  }
  .card--back { top: 23px; }
  .card--front { top: 560px; }

  .mascot {
    position: absolute;
    border-radius: 40px;
    background: linear-gradient(180deg, var(--duck-yellow) 0%, var(--duck-yellow) 55%, var(--flag-blue) 75%, var(--flag-red) 100%);
  }
  .card--back .mascot { left: 70px; top: 50px; width: 250px; height: 300px; }
  .card--front .mascot { left: 580px; top: 130px; width: 270px; height: 330px; }

  .back-copy {
    position: absolute;
    left: 370px;
    top: 60px;
    width: 480px;
    text-align: center;
  }
  .back-title {
    font-size: 30px;
    font-weight: 600;
    color: var(--ink);
    letter-spacing: 0.5px;
    text-transform: uppercase;
  }
  .back-prize {
    margin-top: 14px;
    font-size: 31px;
    font-weight: 700;
    color: var(--prize-red);
    line-height: 1.05;
    text-transform: uppercase;
  }
  .back-story {
    margin-top: 16px;
    font-size: 24px;
    line-height: 1.3;
    color: var(--ink);
  }
  .site-band {
    position: absolute;
    left: 355px;
    top: 400px;
    width: 480px;
    height: 46px;
    background: linear-gradient(180deg, var(--band-blue) 0%, var(--band-blue-dark) 100%);
    color: var(--white);
    font-weight: 700;
    font-size: 20px;
    display: flex;
    align-items: center;
    justify-content: center;
  }

  .event-name {
    position: absolute;
    left: 70px;
    top: 150px;
    width: 480px;
    font-size: 66px;
    font-weight: 800;
    line-height: 1.05;
    color: var(--title-navy);
  }
</style>
</head>
<body>
  <section class="card card--back" aria-label="Card back">
    <div class="mascot" role="img" aria-label="Cartoon duck in sunglasses holding a Colombian flag"></div>
    <div class="back-copy">
      <h2 class="back-title">The Grand Paddle Dash</h2>
      <p class="back-prize">Win 1 of 3 cash prizes<br>totalling $1,000</p>
      <p class="back-story">The Talbrook family is adopting a young girl from Colombia, South America, and needs your help to bring her home</p>
    </div>
    <div class="site-band">www.WelcomingOurLittleOne.example</div>
  </section>

  <section class="card card--front" aria-label="Card front">
    <h1 class="event-name">The Grand Paddle Dash</h1>
    <div class="mascot" role="img" aria-label="Cartoon duck in sunglasses waving a Colombian flag"></div>
  </section>
</body>
</html>
```